Eye-catching Card for new church

I would like a card the size of a business card ... that can be used to announce the start of our new church. I would like it to have our logo on the card, my name, and the statement "Coming Soon ... 1.10.2016". I also would like to list our website address and Facebook page and my Twitter account.

Target Market(s)

prospective people looking for a church

Industry/Entity Type

Church

Requirements
Must have
• a focus on Coming Soon ... 1.10.2016
• Brightfold Church logo
Should not have
• church buildings or writings on the cross

```html
<!DOCTYPE html>
<html lang="en">
<head>
<meta charset="utf-8">
<title>Brightfold Church – Announcement Cards</title>
<link href="https://fonts.googleapis.com/css2?family=Tinos&family=Josefin+Sans:wght@400&display=swap" rel="stylesheet">
<style>
  :root {
    --backdrop: #d9d9d9;
    --card: #f4f4f3;
    --ink: #2b2b2b;
    --ink-soft: #4a4a4a;
    --accent: #1f4fa8;
    --accent-mark: #2a7fd6;
    --wash-dark: #9c9c9c;
    --wash-light: #d6d6d6;
  }
  * { margin: 0; padding: 0; box-sizing: border-box; }
  html, body {
    width: 1200px; height: 900px; overflow: hidden;
    background: var(--backdrop);
  }
  .stage {
    width: 1200px; height: 900px;
    display: flex; align-items: center; justify-content: center; gap: 48px;
  }
  .card {
    position: relative;
    width: 520px; height: 298px;
    background: var(--card);
    box-shadow: 0 6px 18px rgba(0,0,0,.12);
    overflow: hidden;
    display: flex; flex-direction: column; align-items: center; justify-content: center;
  }
  .brush-wash {
    position: absolute;
    left: 90px; top: 40px; width: 360px; height: 210px;
    border-radius: 48% 52% 40% 60% / 55% 45% 55% 45%;
    background: radial-gradient(ellipse at 45% 50%, var(--wash-dark) 0%, #b6b6b6 45%, var(--wash-light) 75%, rgba(214,214,214,0) 100%);
    transform: rotate(-8deg);
    opacity: .85;
  }
  .card > *:not(.brush-wash) { position: relative; }
  .church-name {
    display: flex; align-items: center; gap: 10px;
    font-family: "Tinos", serif;
    font-size: 22px; letter-spacing: 5px; text-transform: uppercase;
    color: var(--ink);
  }
  .church-name .dot {
    width: 14px; height: 14px; border-radius: 50%;
    background: var(--accent-mark);
  }
  .announce {
    margin-top: 14px; text-align: center;
    font-family: "Josefin Sans", sans-serif;
    color: var(--accent);
    font-size: 17px; letter-spacing: 2px; line-height: 1.25;
  }
  .person {
    margin-top: 16px;
    font-family: "Tinos", serif;
    font-size: 26px; letter-spacing: 5px; text-transform: uppercase;
    color: var(--ink);
  }
  .handles {
    margin-top: 6px; text-align: center;
    font-family: "Tinos", serif;
    font-size: 16px; letter-spacing: 2px; line-height: 1.3;
    color: var(--ink-soft);
  }
  .site {
    margin-top: 10px;
    font-family: "Tinos", serif;
    font-size: 12px; letter-spacing: 2px;
    color: var(--ink-soft);
  }
</style>
</head>
<body>
<main class="stage">
  <section class="card card-front">
    <div class="brush-wash" role="img" aria-label="Grey painted brush-stroke texture"></div>
    <div class="church-name"><span class="dot"></span>Brightfold Church</div>
    <p class="announce">COMING SOON<br>1.10.2016</p>
  </section>

  <section class="card card-back">
    <div class="brush-wash" role="img" aria-label="Grey painted brush-stroke texture"></div>
    <div class="church-name"><span class="dot"></span>Brightfold Church</div>
    <p class="person">Your Name Here</p>
    <p class="handles">@twitter<br>/facebook</p>
    <p class="site">www.brightfoldchurch.com</p>
  </section>
</main>
</body>
</html>
```